Frostwyn.co - Arctic & Antarctic Voyages

We need a modern, visually striking business card for Frostwyn.co, a company specialized in selling expedition cruises to the most remote regions on Earth, with a focus on the Arctic and Antarctica. The design should instantly communicate that the cardholder is an expert in polar travel. Use clean, premium aesthetics with cool tones like icy blue and white, possibly incorporating polar imagery (ice, glaciers, penguins, etc.)

Attached the logo

Contact Information for Business Card

Feels high-end and trustworthy.. Visually memorable — encourages people to keep it

Colors
0054AA
0677BA
7BADD7
CADEEF
E8F1F8

Requirements
Must have
• ice, glaciers, penguins, montains
Nice to have
• modern, transparente,

```html
<!DOCTYPE html>
<html lang="en">
<head>
<meta charset="utf-8">
<title>Frostwyn.co – Business Card</title>
<link href="https://fonts.googleapis.com/css2?family=Poppins:wght@700&family=Arimo:wght@400;700&display=swap" rel="stylesheet">
<style>
  :root{
    --deep-blue:#0054AA;
    --brand-blue:#2F75B8;
    --mid-blue:#7BADD7;
    --pale-blue:#CADEEF;
    --ice:#E8F1F8;
    --paper:#FFFFFF;
    --ink:#2B2B2B;
    --backdrop:#B9B9B9;
  }
  *{box-sizing:border-box;margin:0;padding:0}
  html,body{width:1200px;height:788px;overflow:hidden}
  body{
    background:var(--backdrop);
    display:flex;align-items:center;justify-content:center;gap:40px;
    font-family:"Arimo",Arial,sans-serif;
  }
  .card{position:relative;width:560px;height:320px;border-radius:22px;overflow:hidden}

  /* Shared brand block */
  .brand{display:flex;align-items:center;gap:12px}
  .brand__dot{width:30px;height:30px;border-radius:50%;background:var(--brand-blue);flex:none}
  .brand__name{font-family:"Arimo",Arial,sans-serif;font-weight:400;line-height:1;color:var(--deep-blue)}
  .brand__tag{font-family:"Arimo",Arial,sans-serif;font-weight:400;color:var(--ink);letter-spacing:.3px}

  /* Front: contact side */
  .card--front{background:var(--paper)}
  .card--front .decor{
    position:absolute;right:-70px;top:-90px;width:380px;height:380px;border-radius:50%;
    background:radial-gradient(circle at 45% 40%,var(--ice),#DDE7F1);
  }
  .card--front .spark{position:absolute;fill:var(--pale-blue)}
  .card--front .brand{position:absolute;left:34px;top:34px}
  .card--front .brand__name{font-size:34px}
  .card--front .brand__tag{font-size:12.5px;margin-top:6px}
  .accent-bar{position:absolute;left:0;top:150px;width:16px;height:38px;background:var(--brand-blue)}
  .person{position:absolute;left:34px;top:138px;color:var(--ink)}
  .person__name{font-family:"Poppins",sans-serif;font-weight:700;font-size:24px;color:var(--brand-blue);letter-spacing:.5px;line-height:1.05}
  .person__role{font-size:15px;margin-top:2px}
  .person__address{font-size:15px;margin-top:12px;line-height:1.3}
  .contacts{list-style:none;margin-top:12px;font-size:15px;line-height:1.35}
  .contacts li{display:flex;align-items:center;gap:8px}
  .contacts svg{width:12px;height:12px;fill:var(--brand-blue);flex:none}

  /* Back: brand side */
  .card--back{background:var(--brand-blue);display:flex;align-items:center;justify-content:center}
  .card--back .decor{
    position:absolute;left:140px;top:-60px;width:400px;height:400px;border-radius:50%;
    background:radial-gradient(circle at 50% 45%,#4A88C4,#3A7DBE 70%);opacity:.8;
  }
  .card--back .brand{position:relative;gap:18px}
  .card--back .brand__dot{width:60px;height:60px;background:var(--paper)}
  .card--back .brand__name{font-size:58px;color:var(--paper)}
  .card--back .brand__tag{font-size:19px;color:var(--paper);margin-top:8px}
</style>
</head>
<body>
  <section class="card card--front">
    <div class="decor" role="img" aria-label="Faint polar bear and penguin silhouette illustration"></div>
    <svg class="spark" style="left:300px;top:120px" width="22" height="22" viewBox="0 0 20 20"><path d="M10 0l2.5 7.5L20 10l-7.5 2.5L10 20l-2.5-7.5L0 10l7.5-2.5z"/></svg>
    <svg class="spark" style="left:270px;top:170px" width="14" height="14" viewBox="0 0 20 20"><path d="M10 0l2.5 7.5L20 10l-7.5 2.5L10 20l-2.5-7.5L0 10l7.5-2.5z"/></svg>
    <div class="brand">
      <span class="brand__dot"></span>
      <div>
        <div class="brand__name">Frostwyn.co</div>
        <div class="brand__tag">Arctic &amp; Antarctic Voyages</div>
      </div>
    </div>
    <span class="accent-bar"></span>
    <div class="person">
      <div class="person__name">ELIAS MARREN</div>
      <div class="person__role">CEO / Founder</div>
      <div class="person__address">P.O. Box 3190 Harbour Lane<br>Region Name TK 7710</div>
      <ul class="contacts">
        <li><svg viewBox="0 0 24 24"><path d="M6.6 10.8a15 15 0 006.6 6.6l2.2-2.2c.3-.3.7-.4 1-.2 1.1.4 2.3.6 3.6.6.6 0 1 .4 1 1V20c0 .6-.4 1-1 1A17 17 0 013 4c0-.6.4-1 1-1h3.5c.6 0 1 .4 1 1 0 1.3.2 2.5.6 3.6.1.3 0 .7-.2 1z"/></svg>+43 612 48 90 315</li>
        <li><svg viewBox="0 0 24 24"><path d="M2 5h20v14H2zm2 2v.4l8 5 8-5V7z"/></svg>elias.marren@frostwyn.co</li>
        <li><svg viewBox="0 0 24 24"><circle cx="12" cy="12" r="10"/></svg>www.frostwyn.co</li>
      </ul>
    </div>
  </section>

  <section class="card card--back">
    <div class="decor" role="img" aria-label="Faint polar bear and penguin silhouette illustration"></div>
    <div class="brand">
      <span class="brand__dot"></span>
      <div>
        <div class="brand__name">Frostwyn.co</div>
        <div class="brand__tag">Arctic &amp; Antarctic Voyages</div>
      </div>
    </div>
  </section>
</body>
</html>
```